Small dedicated blog website

I have recently had a logo designed for my growing personal hobby, I document my adventures around the world in video form (www.vidstream-example.com/marlowventures.com) I am now trying to create a small blog website with easy access to my other social networks to start to create a home base for all the videos and content I create, I would like a simple website with a focus on blog posts and access to my other social networks, instagram (marlowventures), facebook (marlowventures), snapchat (glenmarlow)

My current website can be viewed at www.marlowventures-example.com

Please contact me for any further information to help this project

Many thanks!

I do not expect a fully coded website, simply designs and graphics

Industry/Entity Type

Social

Font styles to use
Sans Serif

Requirements
Must have
• area for tumblr blog placement, access to social media links

```html
<!DOCTYPE html>
<html lang="en">
<head>
<meta charset="utf-8">
<title>Marlow Ventures — Blog</title>
<link rel="stylesheet" href="https://fonts.googleapis.com/css2?family=Questrial&family=Montserrat:wght@700&family=Arimo&display=swap">
<style>
  :root {
    --page: #2a2a2a;
    --header: #222222;
    --topbar: #b3b3b3;
    --sidebar: #121212;
    --post: #3c3c3c;
    --post-media: #2e2620;
    --white: #ffffff;
    --logo: #d9d9d9;
    --dim: rgba(0, 0, 0, 0.55);
    --modal: rgba(92, 92, 92, 0.9);
    --post-text: #1a1a1a;
  }
  * { box-sizing: border-box; margin: 0; padding: 0; }
  html, body { width: 1200px; height: 1000px; overflow: hidden; }
  body { background: var(--page); position: relative; font-family: "Questrial", sans-serif; }

  .site { position: absolute; left: 88px; top: 0; width: 1024px; height: 1000px; }
  .header { position: absolute; left: 0; top: 0; width: 1024px; height: 248px; background: var(--header); }
  .topbar { position: absolute; left: 233px; top: 0; width: 791px; height: 50px; background: var(--topbar); }
  .brand { position: absolute; right: 47px; top: 168px; display: flex; align-items: center; gap: 8px; }
  .brand-mark { width: 10px; height: 10px; border-radius: 50%; background: var(--logo); }
  .brand-name { font-family: "Montserrat", sans-serif; font-weight: 700; font-size: 15px; color: var(--logo); letter-spacing: 0.4px; }
  .nav-rule { position: absolute; left: 233px; top: 200px; width: 744px; height: 2px; background: var(--white); }
  .nav { position: absolute; left: 233px; top: 209px; width: 744px; height: 40px; font-size: 35px; color: var(--white); }
  .nav a { position: absolute; top: 0; color: inherit; text-decoration: none; }
  .nav .active { font-family: "Montserrat", sans-serif; font-weight: 700; font-size: 30px; top: 2px; left: 22px; }

  .sidebar { position: absolute; left: 0; top: 248px; width: 233px; height: 752px; background: var(--sidebar); }
  .social { position: absolute; left: 150px; width: 46px; height: 46px; border-radius: 50%; border: 2px solid #555; }

  .post { position: absolute; left: 302px; top: 248px; width: 608px; height: 752px; background: var(--post); }
  .post-date { position: absolute; left: 440px; top: 62px; font-family: "Arimo", sans-serif; font-size: 11px; color: #999; }
  .post-media { position: absolute; left: 64px; top: 97px; width: 480px; height: 533px; background: var(--post-media); }
  .post-caption { position: absolute; left: 64px; top: 576px; width: 480px; text-align: center; font-family: "Arimo", sans-serif; font-size: 13px; color: #aaa; }
  .post-body { position: absolute; left: 68px; top: 654px; width: 472px; font-family: "Arimo", sans-serif; font-size: 15.2px; line-height: 19.5px; color: var(--post-text); text-align: justify; hyphens: auto; }

  .dim { position: absolute; left: 0; top: 248px; width: 1200px; height: 752px; background: var(--dim); }

  .modal { position: absolute; left: 121px; top: 281px; width: 957px; height: 554px; background: var(--modal); }
  .modal-text { position: absolute; left: 69px; top: 75px; width: 880px; font-size: 31px; line-height: 36px; letter-spacing: 1.3px; color: var(--white); }
  .modal-text p + p { margin-top: 36px; }
  .thumbs { position: absolute; left: 67px; top: 315px; height: 173px; }
  .thumb { position: absolute; top: 0; width: 268px; height: 173px; }
  .thumb-castle { left: 0; background: linear-gradient(180deg, #8f9395 0%, #8a8c8c 45%, #5a4f45 70%, #3f352c 100%); }
  .thumb-snow { left: 278px; background: linear-gradient(180deg, #6c6a6a 0%, #b6a79a 40%, #2f7fc4 80%, #2668a8 100%); }
  .thumb-card { left: 555px; background: linear-gradient(135deg, #e8e3d6 0%, #dcd6c8 60%, #6b6a66 100%); }
  .close { position: absolute; left: 1065px; top: 268px; width: 27px; height: 27px; }
</style>
</head>
<body>
  <div class="site">
    <header class="header">
      <div class="topbar"></div>
      <div class="brand"><span class="brand-mark"></span><span class="brand-name">MARLOWVENTURES.COM</span></div>
      <div class="nav-rule"></div>
      <nav class="nav">
        <a class="active">BLOG</a>
        <a style="left:252px">VIDEO</a>
        <a style="left:396px">PHOTO</a>
        <a style="left:776px">BIO</a>
      </nav>
    </header>
    <aside class="sidebar">
      <span class="social" style="top:80px"></span>
      <span class="social" style="top:163px"></span>
      <span class="social" style="top:310px"></span>
    </aside>
    <article class="post">
      <p class="post-date">posted tuesday evening</p>
      <div class="post-media" role="img" aria-label="Photo of a travel insurance card"></div>
      <p class="post-caption">insurance sorted, residency forms next</p>
      <p class="post-body">The end of yet another typical Tuesday working behind a reception desk, today I organised my health and travel insurance! I am a Brit&shy;ish citizen but because I'm not a British resident I don't qualify for the European health card, rather expensive but alas had to be done. I also completed the right of residency forms from the Suomi</p>
    </article>
  </div>

  <div class="dim"></div>

  <section class="modal">
    <div class="modal-text">
      <p>I document my various journeys around the world &amp;<br>this website serves as a base for all the media I create.</p>
      <p>I have also recently relocated to finland, so have a<br>click to see what I’m up to!</p>
    </div>
    <div class="thumbs">
      <div class="thumb thumb-castle" role="img" aria-label="Photo of a stone tower on a rocky hill"></div>
      <div class="thumb thumb-snow" role="img" aria-label="Video still of a traveller in a snowy village"></div>
      <div class="thumb thumb-card" role="img" aria-label="Photo of an insurance card close up"></div>
    </div>
  </section>

  <svg class="close" viewBox="0 0 27 27" aria-label="Close">
    <circle cx="13.5" cy="13.5" r="12.5" fill="#000" stroke="#fff" stroke-width="1.2"/>
    <path d="M9 9 L18 18 M18 9 L9 18" stroke="#fff" stroke-width="1.4"/>
  </svg>
</body>
</html>
```